Swimming Pool Business Billboard

10' x 24' Billboard displaying company name, logo and phone number. Picture of swimming pool activity; kids playing , swimming, etc. Bullet points possibly shown: New Construction, Repairs, Weekly maintenance.

Industry/Entity Type

Swimming pool construction, repairs and maintenance.

Font styles to use
Sans Serif

Colors
0054AA
0677BA
7BADD7
CADEEF
E8F1F8

Requirements
Must have
• Rusty & Calder Pembrook, RUSTY'S POOLS & Service,
Nice to have
• Prefer to have my last name "Pembrook" above the word "POOLS" only in smaller print so that "RUSTYS POOLS" is distinguished.

```html
<!DOCTYPE html>
<html lang="en">
<head>
<meta charset="utf-8">
<title>Rusty's Pools &amp; Service – Billboard</title>
<link href="https://fonts.googleapis.com/css2?family=Noto+Serif:ital,wght@0,700;1,600&family=Oswald:wght@600&family=Roboto:wght@500;900&display=swap" rel="stylesheet">
<style>
  :root {
    --page: #e8f1f8;
    --navy: #0c3262;
    --pool-deep: #0677ba;
    --pool-mid: #2fa6d9;
    --pool-light: #7bcbe8;
    --pink: #e5127d;
    --pink-dark: #c81a86;
    --yellow: #fdd20a;
    --white: #ffffff;
  }
  * { margin: 0; padding: 0; box-sizing: border-box; }
  html, body { width: 1200px; height: 840px; overflow: hidden; }
  body { background: var(--page); position: relative; }

  .billboard {
    position: absolute;
    left: 40px; top: 190px;
    width: 1120px; height: 460px;
    overflow: hidden;
    box-shadow: 0 10px 30px rgba(12, 50, 98, .25);
  }
  .pool-backdrop {
    position: absolute; inset: 0;
    background:
      radial-gradient(ellipse at 30% 40%, var(--pool-light) 0%, transparent 55%),
      linear-gradient(160deg, var(--pool-mid) 0%, var(--pool-deep) 100%);
  }

  .owners {
    position: absolute; left: 300px; top: 40px;
    font: italic 600 36px "Noto Serif", serif;
    color: var(--navy);
    white-space: nowrap;
  }
  .brand-name {
    position: absolute; left: 150px; top: 92px;
    font: 700 104px/1 "Noto Serif", serif;
    color: var(--navy);
    letter-spacing: 1px;
    white-space: nowrap;
    text-shadow: 0 2px 6px rgba(255, 255, 255, .45);
  }
  .brand-tagline {
    position: absolute; left: 340px; top: 206px;
    font: 700 92px/1 "Noto Serif", serif;
    color: var(--navy);
    white-space: nowrap;
    text-shadow: 0 2px 6px rgba(255, 255, 255, .45);
  }

  .services-band {
    position: absolute; left: 530px; right: 0; top: 330px; bottom: 0;
    background: var(--yellow);
    padding: 24px 0 0 34px;
    font: 600 38px/1.15 "Oswald", sans-serif;
    color: var(--navy);
    text-transform: uppercase;
  }
  .services-band ul { list-style: none; white-space: nowrap; }
  .services-band li { display: inline; margin-right: 24px; }
  .services-band li::before { content: "• "; }
  .services-band .second-row { display: block; padding-left: 60px; }

  .contact-base {
    position: absolute; left: 0; bottom: 0;
    width: 560px; height: 30px;
    background: var(--navy);
  }
  .contact-pink-edge {
    position: absolute; left: 0; bottom: 30px;
    width: 80px; height: 70px;
    background: var(--pink);
    border-top-right-radius: 30px;
  }
  .call-tab {
    position: absolute; left: 200px; top: 312px;
    height: 42px;
    padding: 0 22px;
    background: var(--navy);
    border-radius: 14px 14px 0 0;
    display: flex; align-items: center;
    font: 500 28px/1 "Roboto", sans-serif;
    color: var(--white);
    white-space: nowrap;
  }
  .phone-block {
    position: absolute; left: 196px; top: 354px;
    width: 344px; height: 80px;
    background: linear-gradient(90deg, var(--pink), var(--pink-dark));
    border-radius: 18px;
    display: flex; align-items: center; justify-content: center;
    font: 900 52px/1 "Roboto", sans-serif;
    color: var(--white);
    white-space: nowrap;
  }
  .brand-badge {
    position: absolute; left: 36px; top: 300px;
    width: 150px; height: 150px;
    border-radius: 50%;
    background: var(--white);
    border: 8px solid var(--navy);
    display: flex; align-items: center; justify-content: center;
    text-align: center;
    font: 900 22px/1.1 "Roboto", sans-serif;
    color: var(--navy);
  }
</style>
</head>
<body>
  <section class="billboard">
    <div class="pool-backdrop" role="img" aria-label="Top-down view of a tiled swimming pool with floating inflatable rings and flowers"></div>

    <p class="owners">Rusty &amp; Calder Pembrook</p>
    <h1 class="brand-name">RUSTY'S POOLS</h1>
    <p class="brand-tagline">&amp; Service</p>

    <div class="services-band">
      <ul>
        <li>New Construction</li><li>Repairs</li>
        <li class="second-row">Weekly Maintenance</li>
      </ul>
    </div>

    <div class="contact-pink-edge"></div>
    <div class="contact-base"></div>
    <div class="call-tab">Call us now!</div>
    <div class="phone-block">912-555-0147</div>
    <div class="brand-badge">RUSTY'S<br>POOLS</div>
  </section>
</body>
</html>
```